Aisle signage for supermarket

Design Isle signs for Indian supermarket. Modern, Clear, legible. Would be nice to use our logo colours. Signs Will be double sided and measure 900mm width x 400mm height. Indian theme would be nice. Attached files shows description to go on each sign.
Font styles to use
Sans Serif
Colors
Designer to choose colors to be used in the design.

```html
<!DOCTYPE html>
<html lang="en">
<head>
<meta charset="utf-8">
<title>Aisle Sign Type Options</title>
<link rel="stylesheet" href="https://fonts.googleapis.com/css2?family=Anton&family=Archivo+Black&family=Audiowide&family=Bowlby+One&family=Graduate&family=Luckiest+Guy&family=Orbitron:wght@400&family=Oswald:wght@700&family=Roboto+Condensed:wght@700&family=Roboto:wght@500;900&family=Russo+One&family=Ultra&display=swap">
<style>
  :root {
    --sign-green: #0b6a35;
    --leaf-green: #8dc63f;
    --lime: #b3d235;
    --badge-green: #7cc142;
    --text-white: #ffffff;
    --rule-grey: #d6d6d6;
    --number-black: #111111;
    --page: #ffffff;
  }
  * { margin: 0; padding: 0; box-sizing: border-box; }
  html, body { width: 868px; height: 1200px; overflow: hidden; background: var(--page); }
  .sheet { position: relative; width: 868px; height: 1200px; }

  .rule-h { position: absolute; left: 0; width: 868px; height: 1px; background: var(--rule-grey); }
  .rule-v { position: absolute; top: 0; left: 433px; width: 1px; height: 1200px; background: var(--rule-grey); }

  .option-number {
    position: absolute;
    font-family: "Oswald", sans-serif;
    font-weight: 700;
    font-size: 42px;
    line-height: 1;
    color: var(--number-black);
    transform: scaleX(0.8);
  }
  .option-number.left { left: 14px; transform-origin: left; }
  .option-number.right { left: 828px; transform-origin: left; }

  .sign { position: absolute; width: 365px; height: 163px; overflow: hidden; background: var(--sign-green); }
  .sign.left { left: 54px; }
  .sign.right { left: 448px; }
  .sign svg { position: absolute; inset: 0; }

  .aisle-list { position: absolute; left: 40px; top: 60px; list-style: none; color: var(--text-white); }
  .aisle-list li { position: relative; padding-left: 14px; height: 24.5px; line-height: 21px; font-size: 16px; white-space: nowrap; }
  .aisle-list li::before {
    content: ""; position: absolute; left: 0; top: 7px;
    border-left: 5px solid var(--text-white);
    border-top: 4px solid transparent; border-bottom: 4px solid transparent;
  }

  .type-1 { font-family: "Luckiest Guy", sans-serif; font-size: 15px !important; letter-spacing: 0.5px; }
  .type-2 { font-family: "Bowlby One", sans-serif; font-size: 14.5px !important; }
  .type-3 { font-family: "Roboto", sans-serif; font-weight: 500; }
  .type-4 { font-family: "Roboto Condensed", sans-serif; font-weight: 700; font-size: 17.5px !important; letter-spacing: -0.3px; }
  .type-5 { font-family: "Ultra", serif; font-size: 13px !important; letter-spacing: -0.3px; }
  .type-6 { font-family: "Graduate", sans-serif; font-size: 17px !important; }
  .type-7 { font-family: "Audiowide", sans-serif; font-size: 14px !important; }
  .type-8 { font-family: "Russo One", sans-serif; font-size: 15.5px !important; letter-spacing: -0.6px; }
  .type-9 { font-family: "Anton", sans-serif; font-size: 19px !important; }
  .type-10 { font-family: "Archivo Black", sans-serif; font-size: 15px !important; }
  .type-11 { font-family: "Orbitron", sans-serif; font-weight: 400; font-size: 14px !important; letter-spacing: -0.3px; }
  .type-12 { font-family: "Roboto", sans-serif; font-weight: 900; font-size: 16.5px !important; letter-spacing: -1px; }

  .row-1 { top: 14px; }  .num-1 { top: 50px; }
  .row-2 { top: 206px; } .num-2 { top: 242px; }
  .row-3 { top: 404px; } .num-3 { top: 440px; }
  .row-4 { top: 602px; } .num-4 { top: 638px; }
  .row-5 { top: 806px; } .num-5 { top: 842px; }
  .row-6 { top: 1014px; } .num-6 { top: 1050px; }
</style>
</head>
<body>
<div class="sheet">
  <svg width="0" height="0" style="position:absolute">
    <defs>
      <g id="sign-art">
        <path d="M0 0 H365 V26 C344 30 326 46 320 72 C315 46 300 36 262 33 H0 Z" fill="var(--leaf-green)" role="img" aria-label="Indian floral pattern band in leaf greens"/>
        <path d="M296 0 C311 12 318 34 320 56 C323 30 333 10 348 0 Z" fill="var(--sign-green)"/>
        <path d="M318 84 L346 112 L318 140 L290 112 Z" fill="var(--badge-green)" stroke="var(--lime)" stroke-width="2"/>
        <path d="M318 90 L340 112 L318 134 L296 112 Z" fill="none" stroke="var(--text-white)" stroke-width="1.2" opacity="0.8"/>
        <text x="318" y="124" text-anchor="middle" font-family="Oswald, sans-serif" font-weight="700" font-size="32" fill="var(--text-white)">1</text>
      </g>
    </defs>
  </svg>

  <div class="rule-v"></div>
  <div class="rule-h" style="top:192px"></div>
  <div class="rule-h" style="top:386px"></div>
  <div class="rule-h" style="top:585px"></div>
  <div class="rule-h" style="top:788px"></div>
  <div class="rule-h" style="top:992px"></div>

  <div class="option-number left num-1">1</div>
  <div class="option-number left num-2">2</div>
  <div class="option-number left num-3">3</div>
  <div class="option-number left num-4">4</div>
  <div class="option-number left num-5">5</div>
  <div class="option-number left num-6">6</div>
  <div class="option-number right num-1">7</div>
  <div class="option-number right num-2">8</div>
  <div class="option-number right num-3">9</div>
  <div class="option-number right num-4">10</div>
  <div class="option-number right num-5">11</div>
  <div class="option-number right num-6">12</div>

  <div class="sign left row-1"><svg viewBox="0 0 365 163"><use href="#sign-art"/></svg>
    <ul class="aisle-list"><li class="type-1">FROZEN</li><li class="type-1">TABLE/COOOKING SAUCES</li><li class="type-1">DESSERT MIXES</li></ul></div>
  <div class="sign left row-2"><svg viewBox="0 0 365 163"><use href="#sign-art"/></svg>
    <ul class="aisle-list"><li class="type-2">FROZEN</li><li class="type-2">TABLE/COOOKING SAUCES</li><li class="type-2">DESSERT MIXES</li></ul></div>
  <div class="sign left row-3"><svg viewBox="0 0 365 163"><use href="#sign-art"/></svg>
    <ul class="aisle-list"><li class="type-3">FROZEN</li><li class="type-3">TABLE/COOOKING SAUCES</li><li class="type-3">DESSERT MIXES</li></ul></div>
  <div class="sign left row-4"><svg viewBox="0 0 365 163"><use href="#sign-art"/></svg>
    <ul class="aisle-list"><li class="type-4">FROZEN</li><li class="type-4">TABLE/COOOKING SAUCES</li><li class="type-4">DESSERT MIXES</li></ul></div>
  <div class="sign left row-5"><svg viewBox="0 0 365 163"><use href="#sign-art"/></svg>
    <ul class="aisle-list"><li class="type-5">FROZEN</li><li class="type-5">TABLE/COOOKING SAUCES</li><li class="type-5">DESSERT MIXES</li></ul></div>
  <div class="sign left row-6"><svg viewBox="0 0 365 163"><use href="#sign-art"/></svg>
    <ul class="aisle-list"><li class="type-6">FROZEN</li><li class="type-6">TABLE/COOOKING SAUCES</li><li class="type-6">DESSERT MIXES</li></ul></div>

  <div class="sign right row-1"><svg viewBox="0 0 365 163"><use href="#sign-art"/></svg>
    <ul class="aisle-list"><li class="type-7">FROZEN</li><li class="type-7">TABLE COOOKING SAUCES</li><li class="type-7">DESSERT MIXES</li></ul></div>
  <div class="sign right row-2"><svg viewBox="0 0 365 163"><use href="#sign-art"/></svg>
    <ul class="aisle-list"><li class="type-8">FROZEN</li><li class="type-8">TABLE/COOOKING SAUCES</li><li class="type-8">DESSERT MIXES</li></ul></div>
  <div class="sign right row-3"><svg viewBox="0 0 365 163"><use href="#sign-art"/></svg>
    <ul class="aisle-list"><li class="type-9">FROZEN</li><li class="type-9">TABLE/COOOKING SAUCES</li><li class="type-9">DESSERT MIXES</li></ul></div>
  <div class="sign right row-4"><svg viewBox="0 0 365 163"><use href="#sign-art"/></svg>
    <ul class="aisle-list"><li class="type-10">FROZEN</li><li class="type-10">TABLE/COOOKING SAUCES</li><li class="type-10">DESSERT MIXES</li></ul></div>
  <div class="sign right row-5"><svg viewBox="0 0 365 163"><use href="#sign-art"/></svg>
    <ul class="aisle-list"><li class="type-11">FROZEN</li><li class="type-11">TABLE/COOOKING SAUCES</li><li class="type-11">DESSERT MIXES</li></ul></div>
  <div class="sign right row-6"><svg viewBox="0 0 365 163"><use href="#sign-art"/></svg>
    <ul class="aisle-list"><li class="type-12">FROZEN</li><li class="type-12">TABLE/COOOKING SAUCES</li><li class="type-12">DESSERT MIXES</li></ul></div>
</div>
</body>
</html>
```